3D Scans and Virtual Tour photography company needs a website

We need a website build that explains what we do, shows some examples of our 3d scans and virtual tours, some stats on why they are important when when selling your home or marketing your business/premises and a contact form to find out more. We need to target both the real estate agents and consumers. The site needs to looks modern, engaging, clean, not lots of text but more pictures and icons. Needs to be mobile friendly. In fact i would build it from the mobile then out.
Updates

Project Deadline Extended
Reason: Hi Team, I have had a couple of requests to extend the Project deadline, which I have now done. I cant push it much more than this as the business is up and running now and I need the website. Looking forward to reviewing the designs.

Target Market(s)

people selling their home and the real estate industry mostly, however any building can be scanned and have a 3d tour

Industry/Entity Type

Photographer

Font styles to use
Sans Serif

Colors
32a6d6
0355a3
33a6d7
85cae6
cee9f5
3176b5

Requirements
Must have
• Our logo
• an example of the 3d scans
• an example of a dollhouse view
• a contact page
• Replace the orange document examples to blue please
• social media links Quillnest Pondlarken Zembol
Nice to have
• some examples of similar companies websites we like
• favourite would be this one hollanbrick (dot com)
• next fav orvantile (dot com au) and brevolux (dot com au)

```html
<!DOCTYPE html>
<html lang="en">
<head>
<meta charset="utf-8">
<title>Tallowmere Imagery — 3D Tours</title>
<link href="https://fonts.googleapis.com/css2?family=Roboto:wght@300;400;500;700&display=swap" rel="stylesheet">
<style>
:root{
  --blue:#32a6d6;
  --blue-deep:#0355a3;
  --blue-mid:#3176b5;
  --blue-soft:#85cae6;
  --blue-pale:#cee9f5;
  --ink:#222;
  --text:#555;
  --muted:#888;
  --line:#e3e3e3;
  --grey-band:#f0f0f0;
  --dark:#3a3a3a;
  --darker:#2b2b2b;
  --white:#fff;
}
*{box-sizing:border-box;margin:0;padding:0}
html,body{width:1200px;height:4986px;overflow:hidden}
body{font-family:'Roboto',Arial,sans-serif;color:var(--text);background:var(--white);position:relative}
section,header,footer,nav{position:relative;width:1200px;overflow:hidden}
.abs{position:absolute}

/* top bar */
.topbar{height:30px;background:#f5f5f5;border-bottom:1px solid var(--line);font-size:11px;color:var(--muted)}
.topbar .welcome{left:73px;top:9px}
.topbar .contact{right:73px;top:9px;display:flex;gap:18px;align-items:center}
.topbar .contact span{display:flex;gap:5px;align-items:center}

/* nav */
.nav{height:96px;background:var(--white);border-bottom:1px solid var(--line)}
.brand{left:73px;top:34px;display:flex;align-items:center;gap:10px}
.brand-dot{width:18px;height:18px;border-radius:50%;background:var(--blue)}
.brand-name{font-size:24px;font-weight:700;color:var(--blue-deep);letter-spacing:.3px}
.menu{right:73px;top:38px;display:flex;gap:32px;font-size:15px;color:var(--ink)}

/* hero */
.hero{height:540px;background:linear-gradient(160deg,#dfeef8 0%,#8fb8d8 35%,#3f6f99 70%,#1f3f60 100%)}
.hero-title{left:0;right:0;top:236px;text-align:center;color:var(--white);font-size:42px;font-weight:300;line-height:1.25}

/* process */
.process{height:425px;background:var(--blue);color:var(--white)}
.process h2{position:absolute;left:0;right:0;top:62px;text-align:center;font-size:24px;font-weight:500}
.process .rail{left:239px;width:718px;top:205px;height:3px;background:var(--white)}
.step{width:240px;text-align:center;top:130px}
.step .ring{width:150px;height:150px;border-radius:50%;background:var(--white);border:6px solid #1f8dc0;margin:0 auto;display:flex;align-items:center;justify-content:center}
.step h3{font-size:19px;font-weight:500;margin-top:22px}
.step p{font-size:14px;line-height:1.4;margin-top:6px}
.duration{top:240px;font-size:15px;width:80px;text-align:center}

/* features */
.features{height:349px}
.features h2{left:73px;top:42px;font-size:26px;font-weight:700;color:var(--ink)}
.feature-list{left:73px;top:104px;list-style:none;width:310px}
.feature-list li{display:flex;gap:18px;align-items:flex-start;font-size:14px;line-height:1.35;color:var(--ink);margin-bottom:15px}
.feature-list svg{flex:0 0 26px}
.plan-art{left:515px;top:24px;width:266px;height:276px;background:linear-gradient(135deg,#d9c7ad,#a8896a 55%,#6f8f5a);clip-path:polygon(50% 0,100% 35%,100% 65%,50% 100%,0 65%,0 35%)}
.try{left:914px;top:92px;width:220px;text-align:center}
.try h3{font-size:22px;font-weight:700;color:var(--blue)}
.try p{font-size:14px;color:var(--ink);margin-top:8px;line-height:1.35}
.btn{display:inline-block;background:var(--blue);color:var(--white);font-weight:500;border-radius:24px;text-align:center}
.try .btn{margin-top:26px;width:150px;height:44px;line-height:44px;font-size:14px}

/* showcase */
.showcase{height:715px;background:linear-gradient(180deg,var(--darker),var(--dark) 60%,#444)}
.showcase h2{left:0;right:0;top:146px;text-align:center;color:var(--white);font-size:24px;font-weight:700}
.device{border-radius:18px;background:#f3f3f3;border:2px solid #d5d5d5;box-shadow:0 10px 30px rgba(0,0,0,.35);padding:20px}
.device .screen{width:100%;height:100%;border-radius:4px;background:linear-gradient(180deg,#e4e4e4 0 12%,#c9b9a6 12% 62%,#fafafa 62%)}
.monitor{left:332px;top:216px;width:632px;height:332px;border-radius:8px;padding:14px}
.tablet-l{left:160px;top:282px;width:305px;height:306px}
.phone-r{left:924px;top:339px;width:133px;height:243px;padding:26px 8px}
.available{left:0;right:0;top:578px;text-align:center;color:var(--white);font-size:13px;font-weight:500}
.partner{top:608px;height:34px;border-radius:4px;background:var(--white)}

/* views */
.views{height:1373px}
.views h2{left:73px;top:24px;font-size:30px;font-weight:700;color:var(--ink)}
.tablet{border-radius:16px;background:#1b1b1b;padding:16px 24px;box-shadow:0 4px 10px rgba(0,0,0,.2)}
.tablet .screen{width:100%;height:100%;background:linear-gradient(180deg,#fff 0 14%,#c8b8a2 14% 80%,#f2f2f2 80%)}
.view-label{display:flex;align-items:center;gap:12px}
.view-label h3{font-size:28px;font-weight:400;color:var(--ink)}
.view-label h3 strong{color:var(--blue);font-weight:400}
.view-sub{font-size:14px;color:var(--ink)}
.stat{left:0;width:1200px;height:86px;background:var(--grey-band);text-align:center;padding-top:16px}
.stat h4{color:var(--blue);font-size:19px;font-weight:400}
.stat p{color:var(--ink);font-size:14px;margin-top:6px}

/* benefit grid */
.benefits{height:866px}
.benefits .vline{top:40px;width:1px;height:790px;background:var(--line)}
.benefits .hline{left:40px;width:1120px;height:1px;top:470px;background:var(--line)}
.benefit{width:300px;text-align:center}
.benefit h3{font-size:19px;font-weight:400;color:var(--ink);margin:18px 0 14px}
.benefit p{font-size:13px;line-height:1.45;color:var(--text)}

/* booking */
.book{height:233px}
.book-photo{left:0;top:0;width:600px;height:233px;background:linear-gradient(110deg,#dde3e9,#9eacb9 60%,#5f6e7d)}
.book-panel{left:600px;top:0;width:600px;height:233px;background:var(--blue);color:var(--white);text-align:center;padding-top:36px}
.book-panel h2{font-size:26px;font-weight:500}
.book-panel .phone-num{font-size:54px;font-weight:500;margin-top:4px;letter-spacing:1px}
.book-panel p{font-size:16px;margin-top:4px}

/* newsletter */
.newsletter{height:77px;background:var(--darker);color:var(--white)}
.newsletter h2{left:73px;top:24px;font-size:22px;font-weight:700}
.newsletter p{left:460px;top:20px;width:500px;font-size:12px;line-height:1.45;color:#ddd}
.newsletter .btn{right:126px;top:20px;width:124px;height:38px;line-height:38px;font-size:14px}

/* footer */
.footer{height:272px;background:var(--white)}
.footer h4{font-size:15px;font-weight:700;color:var(--ink);margin-bottom:10px}
.footer ul{list-style:none;font-size:13px;line-height:1.5;color:var(--text)}
.footer .col{top:24px}
.footer address{font-style:normal;font-size:13px;line-height:1.5;color:var(--text)}
.footer .social{display:flex;gap:12px;margin-top:12px;font-size:12px;color:var(--muted)}
.field{background:#fafafa;border:1px solid #dcdcdc;height:38px;font-size:13px;color:#999;padding:10px 12px}
.submit{background:var(--blue);color:var(--white);font-size:14px;font-weight:500;text-align:center;height:38px;line-height:38px}
.copyright{left:73px;top:246px;font-size:12px;color:var(--muted)}
.footer .rule{left:0;right:0;top:232px;height:1px;background:var(--line)}
</style>
</head>
<body>

<header class="topbar">
  <div class="abs welcome">Welcome to Tallowmere Imagery</div>
  <div class="abs contact">
    <span><svg width="10" height="10" viewBox="0 0 10 10"><path d="M2 0h2l1 3-1.5 1a6 6 0 0 0 2.5 2.5L7 5l3 1v2c0 1-1 2-2 2A8 8 0 0 1 0 2c0-1 1-2 2-2z" fill="#888"/></svg>1800 555 019</span>
    <span><svg width="11" height="9" viewBox="0 0 11 9"><rect x=".5" y=".5" width="10" height="8" fill="none" stroke="#888"/><path d="M.5.5 5.5 5l5-4.5" fill="none" stroke="#888"/></svg>info@tallowmere.com.au</span>
    <span>Quillnest</span><span>Zembol</span><span>Pondlarken</span>
  </div>
</header>

<nav class="nav">
  <div class="abs brand"><div class="brand-dot"></div><div class="brand-name">Tallowmere Imagery</div></div>
  <div class="abs menu"><span>3D Camera</span><span>3D Tours</span><span>Industries</span><span>Virtual Reality</span><span>Support</span><span>Blog</span><span>Contact</span></div>
</nav>

<section class="hero" role="img" aria-label="Upward view of glass skyscrapers against a blue sky">
  <h1 class="abs hero-title">Transform your business through<br>the power of immersive media</h1>
</section>

<section class="process">
  <h2>Our Process</h2>
  <div class="abs rail"></div>
  <div class="abs duration" style="left:382px">2 hrs</div>
  <div class="abs duration" style="left:741px">48 hrs</div>
  <div class="abs step" style="left:119px">
    <div class="ring"><svg width="60" height="58" viewBox="0 0 44 44" fill="none" stroke="#32a6d6" stroke-width="3"><rect x="4" y="11" width="36" height="26" rx="3"/><path d="M15 11l3-5h8l3 5"/><circle cx="22" cy="24" r="7"/></svg></div>
    <h3>Scan</h3><p>Capture a space<br>in <b>3D</b></p>
  </div>
  <div class="abs step" style="left:478px">
    <div class="ring"><svg width="64" height="58" viewBox="0 0 48 44" fill="none" stroke="#32a6d6" stroke-width="3"><path d="M14 34H11a9 9 0 0 1 0-18 12 12 0 0 1 23-2 10 10 0 0 1 3 20h-3"/><path d="M24 38V20M17 27l7-7 7 7"/></svg></div>
    <h3>Upload</h3><p>Process &amp; Store<br>in the <b>Cloud</b></p>
  </div>
  <div class="abs step" style="left:837px">
    <div class="ring"><svg width="40" height="64" viewBox="0 0 30 48" fill="none" stroke="#32a6d6" stroke-width="3"><rect x="2" y="2" width="26" height="44" rx="4"/><path d="M2 9h26M2 38h26"/></svg></div>
    <h3>View</h3><p>Experience via<br><b>Web &amp; Mobile</b></p>
  </div>
</section>

<section class="features">
  <h2 class="abs">Complementary Features</h2>
  <ul class="abs feature-list">
    <li><svg width="26" height="22" viewBox="0 0 26 22" fill="none" stroke="#3176b5" stroke-width="2"><rect x="1" y="1" width="24" height="20"/><path d="M1 7h24"/></svg>1. 3D Tour (Integrated into Homeward and keyfinder.com.au)</li>
    <li><svg width="26" height="22" viewBox="0 0 26 22" fill="none" stroke="#3176b5" stroke-width="2"><rect x="1" y="1" width="24" height="20"/><path d="M10 1v12h15"/></svg>2. Traditional Floor Plan (With Measurements)</li>
    <li><svg width="26" height="22" viewBox="0 0 26 22" fill="none" stroke="#3176b5" stroke-width="2"><rect x="1" y="1" width="24" height="20"/><path d="M5 7h16M5 12h16M5 17h10"/></svg>3. Company branding and digital presence</li>
    <li><svg width="26" height="22" viewBox="0 0 26 22" fill="none" stroke="#3176b5" stroke-width="2"><rect x="1" y="1" width="24" height="20"/><path d="M6 16v-4M12 16V8M18 16V5"/></svg>4. Fortnightly analytic reports</li>
    <li><svg width="26" height="22" viewBox="0 0 26 22" fill="none" stroke="#3176b5" stroke-width="2"><rect x="1" y="1" width="24" height="20"/><path d="M8 8l-4 3 4 3M18 8l4 3-4 3"/></svg>5. Leading web integration and backend support</li>
  </ul>
  <div class="abs plan-art" role="img" aria-label="Furnished 3D dollhouse floor plan of an apartment"></div>
  <div class="abs try">
    <h3>Try it for yourself</h3>
    <p>Hit the Start 3D button to experience our feature tour</p>
    <span class="btn">START 3D</span>
  </div>
</section>

<section class="showcase">
  <h2 class="abs">Stop Buyers In Their Tracks With An Engaging 3D Tour.</h2>
  <div class="abs device monitor" role="img" aria-label="Property listing site with 3D tour shown on a desktop monitor"><div class="screen"></div></div>
  <div class="abs device tablet-l" role="img" aria-label="Property listing site shown on a tablet"><div class="screen"></div></div>
  <div class="abs device phone-r" role="img" aria-label="Property listing site shown on a phone"><div class="screen"></div></div>
  <div class="abs available">Available On</div>
  <div class="abs partner" style="left:440px;width:150px"></div>
  <div class="abs partner" style="left:612px;width:150px"></div>
</section>

<section class="views">
  <h2 class="abs">Stand Out Online By Attracting The Right Buyers.</h2>

  <div class="abs tablet" style="left:140px;top:86px;width:266px;height:219px" role="img" aria-label="Tablet showing a live floor plan of a property"><div class="screen"></div></div>
  <div class="abs" style="left:632px;top:160px">
    <div class="view-label"><svg width="44" height="44" viewBox="0 0 44 44" fill="none" stroke="#32a6d6" stroke-width="3"><path d="M2 2h40v40H2zM2 22h18V2M20 30v12"/></svg><h3>Live <strong>Floor</strong> Plan</h3></div>
    <p class="view-sub" style="margin:18px 0 0 56px">Examine the property from above.</p>
  </div>
  <div class="abs stat" style="top:372px"><h4>Buyers Love 3D Tours!</h4><p>80% increase in enquiries for properties with 3D Tours</p></div>

  <div class="abs" style="left:73px;top:578px">
    <div class="view-label"><svg width="56" height="44" viewBox="0 0 56 44" fill="none" stroke="#32a6d6" stroke-width="3"><path d="M4 14 28 2l24 12-24 12zM4 14v16l24 12 24-12V14M28 26v16"/></svg><h3>3D <strong>Dollhouse</strong> View</h3></div>
    <p class="view-sub" style="margin-top:14px">View the property in three dimensions</p>
  </div>
  <div class="abs tablet" style="left:698px;top:522px;width:359px;height:259px" role="img" aria-label="Tablet showing a 3D dollhouse view of a home"><div class="screen"></div></div>
  <div class="abs stat" style="top:830px;height:77px;padding-top:10px"><h4>Online Engagement</h4><p>Users spend 52% longer on listings featuring 3D Tours</p></div>

  <div class="abs tablet" style="left:140px;top:956px;width:266px;height:256px" role="img" aria-label="Tablet showing a first person view inside a living room"><div class="screen"></div></div>
  <div class="abs" style="left:632px;top:1032px">
    <div class="view-label"><svg width="44" height="48" viewBox="0 0 44 48" fill="none" stroke="#32a6d6" stroke-width="3"><rect x="2" y="2" width="40" height="44"/><circle cx="20" cy="12" r="4" fill="#32a6d6"/><path d="M20 18v12l-6 10M20 30l6 10M14 24h12"/></svg><h3>First <strong>Person</strong> View</h3></div>
    <p class="view-sub" style="margin:16px 0 0 56px">Experience the property as if you were physically there</p>
  </div>
  <div class="abs stat" style="top:1270px;height:84px;padding-top:14px"><h4>Better Than Video</h4><p>3D Tours provide 4x engagement compared to video</p></div>
</section>

<section class="benefits">
  <div class="abs vline" style="left:419px"></div>
  <div class="abs vline" style="left:778px"></div>
  <div class="abs hline"></div>

  <div class="abs benefit" style="left:90px;top:130px">
    <svg width="70" height="66" viewBox="0 0 70 66" fill="none" stroke="#32a6d6" stroke-width="3"><path d="M6 32 35 4l29 28M14 24v38h42V24M28 62V42h14v20"/></svg>
    <h3>Integration</h3><p>With the 3D Tour integration across online real estate portals, the property will stand out instantly from the search results with the bold 3D icon. Click here to see what it looks like</p>
  </div>
  <div class="abs benefit" style="left:448px;top:130px">
    <svg width="70" height="66" viewBox="0 0 70 66" fill="none" stroke="#32a6d6" stroke-width="3"><circle cx="35" cy="30" r="26"/><circle cx="24" cy="26" r="5"/><circle cx="46" cy="26" r="5"/><path d="M29 26h12M35 56v8"/></svg>
    <h3>Connect</h3><p>A 3D Tour allows for genuine buyers to build an emotional connection with the property</p>
  </div>
  <div class="abs benefit" style="left:807px;top:130px">
    <svg width="70" height="66" viewBox="0 0 70 66" fill="none" stroke="#32a6d6" stroke-width="3"><circle cx="35" cy="33" r="29"/><path d="M35 14v19l12 8"/></svg>
    <h3>Time</h3><p>Buyers spend an additional 3-4 minutes engaged in a listing with a 3D Tour compared to those without</p>
  </div>

  <div class="abs benefit" style="left:90px;top:510px">
    <svg width="70" height="66" viewBox="0 0 70 66"><circle cx="35" cy="33" r="30" fill="#32a6d6"/><path d="M20 16c8 4 4 10 12 12s4 10-2 14M44 10c-4 8 4 10 10 12M40 50c4-6 10-6 14-2" fill="none" stroke="#fff" stroke-width="3"/></svg>
    <h3>Share</h3><p>3D Tours allow for immersive interaction with the property for remote and overseas buyers</p>
  </div>
  <div class="abs benefit" style="left:448px;top:510px">
    <svg width="70" height="66" viewBox="0 0 70 66"><text x="35" y="58" text-anchor="middle" font-family="Roboto, sans-serif" font-size="66" font-weight="700" fill="#32a6d6">$</text></svg>
    <h3>Value</h3><p>Perceived value of the property increases as a direct result of sophisticated marketing</p>
  </div>
  <div class="abs benefit" style="left:807px;top:510px">
    <svg width="70" height="66" viewBox="0 0 70 66" fill="#32a6d6"><rect x="8" y="40" width="10" height="22"/><rect x="22" y="30" width="10" height="32"/><rect x="36" y="34" width="10" height="28"/><rect x="50" y="16" width="10" height="46"/><path d="M8 30 26 16l14 8L60 4" fill="none" stroke="#32a6d6" stroke-width="3"/></svg>
    <h3>Analytics</h3><p>Detailed analytics allows assessment of traffic to 3D Tours in real time</p>
  </div>
</section>

<section class="book">
  <div class="abs book-photo" role="img" aria-label="Person wearing a virtual reality headset"></div>
  <div class="abs book-panel">
    <h2>Book Your 3D Tour Today!</h2>
    <div class="phone-num">1800 555 019</div>
    <p>info@tallowmere.com.au</p>
  </div>
</section>

<section class="newsletter">
  <h2 class="abs">Sign Up Our Newsletter!</h2>
  <p class="abs">Sign up today for our newsletter and receive latest news and also get our tips &amp; exclusive offers.</p>
  <span class="abs btn">SIGN UP</span>
</section>

<footer class="footer">
  <div class="abs col" style="left:73px">
    <h4>Quick Links</h4>
    <ul><li>3D Camera</li><li>3D Tours</li><li>Industries</li><li>Virtual Reality</li><li>Support</li><li>Blog</li><li>Contact</li></ul>
  </div>
  <div class="abs col" style="left:249px">
    <h4>Tallowmere Imagery</h4>
    <address>88 Calder Street Suite 12<br>Brookvale 2100<br><br>T: 1800 555 019<br>E: info@tallowmere.com.au</address>
    <div class="social"><span>Quillnest</span><span>Zembol</span><span>Pondlarken</span></div>
  </div>
  <div class="abs col" style="left:522px">
    <h4>Leave A Message</h4>
  </div>
  <div class="abs field" style="left:522px;top:62px;width:236px">Name</div>
  <div class="abs field" style="left:522px;top:108px;width:236px">Email</div>
  <div class="abs field" style="left:522px;top:154px;width:236px">Phone</div>
  <div class="abs field" style="left:771px;top:62px;width:353px;height:84px">Message</div>
  <div class="abs submit" style="left:771px;top:154px;width:353px">SUBMIT</div>
  <div class="abs rule"></div>
  <div class="abs copyright">©2017 Tallowmere Imagery. All rights reserved</div>
</footer>

</body>
</html>
```